Business Card Design Project

Hi,

We need new business cards for our company The Brightmere Trading
www.thebrightmeretrading.example

Clean design

We will be focussing a lot on social media and online business in 2013.

All our social media channels should be included
Trellisly Group or Trellisly Company Page ,Wavetome Page,Zentro and website

Mobile number, general telephone number,emailadress, street address etc

On the back of the card we want to promote our Velder Institute Coaching Workshops (we do this via our Plomvista page) with a place for a unique voucher code (reduction of 75 € for a coaching workshop of your choice) for every card

We would like to have our personal photo's in it.

Designs should be easy to adapt afterwards (when we hire new people - new pictures etc.)

We would like to work with Zel as business cards service

Target Market(s)

All B2B Professionals

Industry/Entity Type

Business

Requirements
Nice to have
• QR code?

```html
<!DOCTYPE html>
<html lang="en">
<head>
<meta charset="utf-8">
<title>The Brightmere Trading – Business Card</title>
<link href="https://fonts.googleapis.com/css2?family=Ubuntu:wght@400;500;700&display=swap" rel="stylesheet">
<style>
  :root {
    --brand-blue: #2a96d2;
    --brand-blue-light: #7cc3ea;
    --brand-navy: #2f3f8f;
    --ink: #3c4247;
    --ink-soft: #6b7278;
    --paper: #ffffff;
    --backdrop: #dfe5ea;
  }
  * { margin: 0; padding: 0; box-sizing: border-box; }
  html, body { width: 1200px; height: 960px; overflow: hidden; }
  body {
    background: var(--backdrop);
    font-family: "Ubuntu", sans-serif;
    color: var(--ink);
    position: relative;
  }
  .card {
    position: absolute;
    left: 250px;
    width: 700px;
    height: 400px;
    background: var(--paper);
    overflow: hidden;
    box-shadow: 0 6px 18px rgba(40, 60, 80, 0.18);
  }
  .card--front { top: 50px; }
  .card--back { top: 505px; }

  .card__top-strip {
    position: absolute; left: 0; top: 0; width: 100%; height: 18px;
    background: var(--brand-blue);
  }
  .card__bottom-band {
    position: absolute; left: 0; bottom: 0; width: 100%;
    background: var(--brand-blue);
  }
  .card--front .card__bottom-band { height: 150px; }
  .card--back .card__bottom-band { height: 125px; }

  /* Front */
  .address {
    position: absolute; left: 40px; top: 50px;
    font-size: 17px; color: var(--ink);
  }
  .brand-mark-small {
    position: absolute; right: 34px; top: 30px;
    width: 62px; height: 62px; border-radius: 50%;
    background: var(--brand-blue-light);
  }
  .portrait {
    position: absolute; left: 40px; top: 112px;
    width: 214px; height: 256px;
    border: 3px solid var(--brand-blue);
    background: linear-gradient(180deg, #eceeef 0%, #d9d3cf 55%, #8a5a45 100%);
  }
  .contact-list {
    position: absolute; left: 330px; top: 96px;
    list-style: none;
  }
  .contact-list li {
    display: flex; align-items: center;
    height: 21px; font-size: 15px; color: var(--ink);
  }
  .contact-list svg { width: 14px; height: 14px; margin-right: 16px; flex: none; }
  .person {
    position: absolute; left: 338px; top: 276px; color: var(--paper);
  }
  .person__name { font-size: 27px; font-weight: 400; }
  .person__role { font-size: 18px; margin-top: 6px; }

  /* Back */
  .brand-lockup {
    position: absolute; left: 0; top: 72px; width: 100%;
    display: flex; align-items: center; justify-content: center; gap: 22px;
  }
  .brand-lockup__dot {
    width: 110px; height: 110px; border-radius: 50%;
    background: var(--brand-blue-light);
  }
  .brand-lockup__name {
    font-size: 34px; font-weight: 700; line-height: 1.05;
    color: var(--brand-navy);
  }
  .voucher {
    position: absolute; left: 50%; bottom: 40px; transform: translateX(-50%);
    width: 300px; height: 44px; border-radius: 10px;
    border: 2px dashed rgba(255,255,255,0.85);
    background: linear-gradient(180deg, #9fd4f1 0%, #6cb8e3 100%);
    display: flex; align-items: center; justify-content: center;
    font-size: 21px; letter-spacing: 1px; color: #4a5258;
  }
</style>
</head>
<body>

<section class="card card--front" aria-label="Business card front">
  <div class="card__top-strip"></div>
  <div class="card__bottom-band"></div>
  <p class="address">Lindenlaan 24, 1830 Vermeldorp (Brussels Area), Belgium</p>
  <div class="brand-mark-small" aria-hidden="true"></div>
  <div class="portrait" role="img" aria-label="Portrait photo of the card holder"></div>

  <ul class="contact-list">
    <li>
      <svg viewBox="0 0 14 14" aria-hidden="true"><path d="M3 1 L5 1 L6 4 L4.5 5.5 Q6 8.5 8.5 9.5 L10 8 L13 9 L13 11 Q12 13 10 13 Q2 11 1 3 Q1 1 3 1 Z" fill="var(--brand-blue)"/></svg>
      0400 555 018
    </li>
    <li>
      <svg viewBox="0 0 14 14" aria-hidden="true"><rect x="3.5" y="1" width="7" height="12" rx="1.2" fill="var(--brand-blue)"/><rect x="4.8" y="2.5" width="4.4" height="7" fill="#fff"/></svg>
      0400 555 018
    </li>
    <li>
      <svg viewBox="0 0 14 14" aria-hidden="true"><rect x="1" y="3" width="12" height="9" fill="var(--brand-blue)"/><path d="M1 3 L7 8 L13 3" stroke="#fff" stroke-width="1.2" fill="none"/></svg>
      info@thebrightmeretrading.example
    </li>
    <li>
      <svg viewBox="0 0 14 14" aria-hidden="true"><circle cx="7" cy="7" r="6" fill="var(--brand-blue)"/><path d="M1 7 H13 M7 1 Q3.5 7 7 13 M7 1 Q10.5 7 7 13" stroke="#fff" stroke-width="1" fill="none"/></svg>
      www.thebrightmeretrading.example
    </li>
    <li>
      <svg viewBox="0 0 14 14" aria-hidden="true"><rect x="1" y="1" width="12" height="12" rx="2" fill="var(--brand-blue)"/></svg>
      /thebrightmeretrading
    </li>
    <li>
      <svg viewBox="0 0 14 14" aria-hidden="true"><rect x="1" y="1" width="12" height="12" rx="2" fill="var(--brand-blue)"/></svg>
      @brightmeretrading
    </li>
    <li>
      <svg viewBox="0 0 14 14" aria-hidden="true"><rect x="1" y="1" width="12" height="12" rx="2" fill="var(--brand-blue)"/></svg>
      brightmere-inner-circle
    </li>
  </ul>

  <div class="person">
    <p class="person__name">Daniel Ashcombe</p>
    <p class="person__role">Manager</p>
  </div>
</section>

<section class="card card--back" aria-label="Business card back">
  <div class="card__top-strip"></div>
  <div class="card__bottom-band"></div>
  <div class="brand-lockup">
    <div class="brand-lockup__dot" aria-hidden="true"></div>
    <p class="brand-lockup__name">The<br>Brightmere<br>Trading</p>
  </div>
  <div class="voucher">voucher code</div>
</section>

</body>
</html>
```